CREATE A KILLER WEBSITE DESIGN

We are a firearms training company that trains CIVILIANS (no police or military pictures - thank you!) to defend themselves and are looking for a killer design that's clean, easy to navigate and modern! We want the newest trends applied to this sight like a scrollable site so you can scroll down and see all the features. We are okay with tweaking the HTML but need the artistic design to look good. I'll provide a link to our current site along with a sight we really like so you can get an idea!

I'm supplying a PowerPoint Design we are going with from another designer so you can match the style to the new site.

PAGES: (Please use information from our current site. We like the information but just want a more polished look similar to the NWDLA site below but in our colors.)
Home - Long Form Scrolling Site. Top fold will be a video with a play button.
Falcon Institute - Seven Level Training Program Info Page That Will Contain A Video.
Contact Us - This will be a page that DOES NOT CONTAIN AN EMAIL ADDRESS. Just a contact us form
Meet The Trainer: Morgan Pellbrook

Our site:
https://www.brisklanewardens.biz

Sights We Like:
https://www.nwdefenseleague.example.com
https://quorvel.example.com
https://brantforgeworks.example.com
https://www.pelnrigear.example.com

Target Market(s)

Men and women ages 21 to 100 years old

Industry/Entity Type

Self Defense

Number of Pages Required

5+ page

Font styles to use
Sans Serif

Colors
f26267

Requirements
Must have
• Clean and engaging. Use of colors that match our logo.
Should not have
• Poor design quality

```html
<!DOCTYPE html>
<html lang="en">
<head>
<meta charset="utf-8">
<title>Brisklane Wardens – Home</title>
<link href="https://fonts.googleapis.com/css2?family=Barlow:wght@400;500;600;700&family=Michroma&display=swap" rel="stylesheet">
<style>
:root{
  --red:#e5201f;
  --black:#0b0b0b;
  --ink:#1d1d1d;
  --muted:#555;
  --gray-bg:#ececec;
  --band:#e2e2e2;
  --white:#fff;
  --star:#f08a1c;
}
*{box-sizing:border-box;margin:0;padding:0}
html,body{width:1200px;height:3545px;overflow:hidden}
body{position:relative;font-family:'Barlow',sans-serif;color:var(--ink);background:var(--white)}
.abs{position:absolute}
.display{font-family:'Michroma',sans-serif;text-transform:uppercase;letter-spacing:0}
.red{color:var(--red)}

/* header */
.site-header{left:0;top:0;width:1200px;height:120px;background:var(--black)}
.brand{left:88px;top:34px;display:flex;align-items:center;gap:10px;color:var(--white);font-weight:700;font-size:22px}
.brand-dot{width:26px;height:26px;border-radius:50%;background:var(--red)}
.toll{left:650px;top:30px;font-size:17px;font-weight:500;color:var(--white)}
.toll span{color:var(--red)}
.login{left:860px;top:32px;font-size:12px;color:#ccc;letter-spacing:.5px;display:flex;gap:5px;align-items:center}
.cart{left:940px;top:24px;width:32px;height:32px;border:1.5px solid var(--red);border-radius:50%}
.cart-count{left:962px;top:22px;width:14px;height:14px;border-radius:50%;background:var(--red);color:#fff;font-size:8px;text-align:center;line-height:14px}
.btn-red{background:var(--red);color:#fff;border-radius:20px;font-size:12px;font-weight:700;text-align:center;letter-spacing:.4px}
.contact-btn{left:1000px;top:25px;width:112px;height:32px;line-height:32px}
.main-nav{left:360px;top:83px;width:752px;display:flex;justify-content:space-between;font-size:12.5px;font-weight:700;color:#fff;letter-spacing:.3px}
.main-nav .active{color:var(--red)}

/* hero */
.hero{left:0;top:120px;width:1200px;height:440px;background:linear-gradient(100deg,#3a342a 0%,#6b5e45 35%,#4a4433 60%,#2c2a22 100%)}
.hero-play{left:578px;top:271px}
.hero-quote{left:0;top:338px;width:1200px;text-align:center;color:#fff;font-size:28px;font-weight:700;line-height:35px}

/* levels */
.section-title{left:0;width:1200px;text-align:center;font-size:24px;line-height:35px}
.levels-line{left:92px;top:774px;width:1016px;border-top:1px dashed #bbb}
.levels-end{top:770px;width:9px;height:9px;border-radius:50%;background:#999}
.level{width:160px;top:735px;text-align:center}
.level-num{width:80px;height:80px;margin:0 auto;border-radius:50%;background:#fff;box-shadow:0 2px 10px rgba(0,0,0,.12);color:var(--red);font-size:38px;line-height:80px;font-weight:500}
.level-name{margin-top:28px;font-size:13.5px;font-weight:700;line-height:17px}
.pill{height:30px;line-height:28px;border-radius:18px;font-size:12px;font-weight:600;text-align:center}
.pill-outline{border:1.5px solid var(--red);color:var(--red);background:#fff}

/* gray band */
.gray-band{left:0;top:1197px;width:1200px;height:760px;background:linear-gradient(135deg,#f1f1f1,#e4e4e4 50%,#efefef)}
.video{left:208px;top:1017px;width:784px;height:359px;background:radial-gradient(circle at 50% 45%,#1d3b5c 0%,#0d1a2a 35%,#05070a 70%);border-radius:2px}
.video-play{left:578px;top:1175px}

/* instructor */
.about-kicker{left:143px;top:1453px;font-size:13px;letter-spacing:.5px;color:#333}
.about-name{left:143px;top:1476px;font-size:23px}
.mini-brand{left:1000px;top:1478px;display:flex;gap:8px;align-items:center;font-size:14px;font-weight:700}
.mini-brand i{width:14px;height:14px;background:var(--red);border-radius:50%;display:block}
.portrait{left:88px;top:1559px;width:320px;height:320px;border-radius:50%;border:3px solid var(--red);background:radial-gradient(circle at 50% 40%,#bdbdbd,#5a5a5a 75%)}
.bio{left:472px;top:1562px;width:640px;font-size:13.3px;line-height:19.3px;color:#222}
.seen-band{left:413px;top:1768px;width:659px;height:110px;background:var(--band)}
.seen-label{left:472px;top:1814px;font-size:16px}
.badge{top:1783px;width:80px;height:80px;border-radius:50%;background:#fff;box-shadow:0 2px 6px rgba(0,0,0,.08)}
.badge::after{content:"";position:absolute;left:22px;top:22px;width:36px;height:36px;border-radius:8px;background:#c9c9c9}

/* testimonials */
.card{top:2094px;width:319px;height:311px;background:#fff;box-shadow:0 1px 8px rgba(0,0,0,.1);text-align:center;padding:0 24px}
.card .q{margin-top:34px;color:var(--red);font-size:46px;font-weight:700;line-height:30px;font-family:Georgia,serif}
.card p{margin-top:24px;font-size:12.5px;line-height:19.3px;color:#333;height:112px}
.card .stars{color:var(--star);font-size:19px;letter-spacing:2px}
.card .who{margin-top:6px;font-size:13.5px;font-weight:700}
.card .when{font-size:12.5px;color:#444}

/* contact */
.contact-band{left:0;top:2559px;width:1200px;height:596px;background:linear-gradient(135deg,#efefef,#e0e0e0 55%,#ececec)}
.q-item{top:2697px;width:240px;text-align:center;font-size:19px;line-height:22px}
.q-item svg{display:block;margin:0 auto 10px}
.q-item .l1{color:var(--red)}
.field{background:#fff;border-radius:16px;font-size:11px;color:#444;padding:7px 14px}
.send{left:535px;top:3051px;width:145px;height:31px;line-height:31px}

/* footer */
.footer{left:0;top:3155px;width:1200px;height:390px;background:var(--black);color:#ddd}
.f-brand{left:88px;top:3270px;color:#fff;font-weight:700;font-size:18px;display:flex;gap:8px;align-items:center}
.f-brand i{width:18px;height:18px;border-radius:50%;background:var(--red);display:block}
.f-about{left:88px;top:3322px;width:240px;font-size:11.5px;line-height:17px}
.f-head{font-size:12.5px;font-weight:700;color:var(--red);letter-spacing:.4px}
.f-call{left:367px;top:3252px;font-size:22px;color:#fff}
.f-mail{left:367px;top:3281px;font-size:12px;text-decoration:underline;color:#fff}
.f-addr{left:367px;top:3349px;font-size:12px;line-height:18px}
.f-list{list-style:none;font-size:12px;line-height:23.2px}
.f-list .on{color:var(--red)}
.social{left:1078px;width:32px;height:32px;border:1.5px solid var(--red);border-radius:50%}
.social.fill{background:var(--red)}
.f-rule{left:55px;top:3461px;width:1090px;border-top:1px solid #333}
.copy{left:88px;top:3495px;font-size:12px}
.to-top{left:1078px;top:3489px;width:32px;height:32px;border-radius:50%;background:var(--red)}
</style>
</head>
<body>

<header class="site-header abs">
  <div class="brand abs"><i class="brand-dot"></i>Brisklane Wardens</div>
  <div class="toll abs"><span>Toll-Free:</span> 855-I-Am-Ready</div>
  <div class="login abs"><svg width="12" height="12" viewBox="0 0 12 12"><circle cx="6" cy="6" r="5" fill="none" stroke="#e5201f"/><circle cx="6" cy="5" r="2" fill="#e5201f"/></svg>LOGIN</div>
  <div class="cart abs"><svg width="29" height="29" viewBox="0 0 29 29"><path d="M9 12h11l-1.5 6h-8z" fill="none" stroke="#e5201f" stroke-width="1.4"/></svg></div>
  <div class="cart-count abs">01</div>
  <div class="contact-btn btn-red abs">CONTACT US</div>
  <nav class="main-nav abs">
    <span class="active">HOME</span><span>FALCON INSTITUTE</span><span>ABOUT</span><span>TESTIMONIALS</span><span>SHOP</span><span>UPCOMING CLASSES</span><span>VIDEOS</span><span>LOST CERTIFICATE</span>
  </nav>
</header>

<section class="hero abs" role="img" aria-label="Video still of a civilian shooter training at an outdoor range with silhouette targets"></section>
<svg class="hero-play abs" width="44" height="44" viewBox="0 0 44 44"><circle cx="22" cy="22" r="20" fill="none" stroke="#fff" stroke-width="2.5"/><path d="M17 13l13 9-13 9z" fill="none" stroke="#fff" stroke-width="2.5" stroke-linejoin="round"/></svg>
<h1 class="hero-quote abs">"Your Life May &nbsp;Depend On What You Learn In Your<br>Concealed Carry Training - Don't Settle For A Gun Shop Class!"</h1>

<h2 class="section-title display abs" style="top:632px"><span class="red">Our 7 Levels of Training</span> Take You<br>From Zero To Hero</h2>
<div class="levels-line abs"></div>
<div class="levels-end abs" style="left:88px"></div>
<div class="levels-end abs" style="left:1103px"></div>
<div class="level abs" style="left:81px"><div class="level-num">1</div><div class="level-name">Concealed Carry<br>Class</div></div>
<div class="level abs" style="left:227px"><div class="level-num">2</div><div class="level-name">Dynamic Defensive<br>Shooting</div></div>
<div class="level abs" style="left:374px"><div class="level-num">3</div><div class="level-name">Fine Tuning Your<br>Technique</div></div>
<div class="level abs" style="left:520px"><div class="level-num">4</div><div class="level-name">Virtual Threat<br>Lab</div></div>
<div class="level abs" style="left:666px"><div class="level-num">5</div><div class="level-name">Tactical Skills and<br>Drills</div></div>
<div class="level abs" style="left:812px"><div class="level-num">6</div><div class="level-name">Close Quarters<br>Defense</div></div>
<div class="level abs" style="left:959px"><div class="level-num">7</div><div class="level-name">Live Scenario<br>Threat-Lab</div></div>
<div class="pill btn-red abs" style="left:453px;top:907px;width:141px;line-height:30px">FALCON INSTITUTE</div>
<div class="pill pill-outline abs" style="left:604px;top:907px;width:143px">GET TICKETS NOW</div>

<div class="gray-band abs"></div>
<div class="video abs" role="img" aria-label="Video still: the earth in space with a production title card"></div>
<svg class="video-play abs" width="44" height="44" viewBox="0 0 44 44"><circle cx="22" cy="22" r="20" fill="none" stroke="#fff" stroke-width="2.5"/><path d="M17 13l13 9-13 9z" fill="none" stroke="#fff" stroke-width="2.5" stroke-linejoin="round"/></svg>

<svg class="abs" style="left:88px;top:1464px" width="30" height="30" viewBox="0 0 30 30"><circle cx="15" cy="15" r="13" fill="none" stroke="#e5201f" stroke-width="2"/><circle cx="15" cy="15" r="8" fill="none" stroke="#e5201f" stroke-width="2"/><circle cx="15" cy="15" r="3" fill="#e5201f"/></svg>
<div class="about-kicker abs">ABOUT THE INSTRUCTOR</div>
<h2 class="about-name display abs"><span class="red">Morgan</span> Pellbrook</h2>
<div class="mini-brand abs"><i></i>Brisklane Wardens</div>
<div class="portrait abs" role="img" aria-label="Black and white portrait of instructor Morgan Pellbrook"></div>
<p class="bio abs">Morgan Pellbrook is a 3rd generation Jacksonville native and delighted to be a part of this great community. He is a true security expert with 25 years of experience in the security industry. He has appeared on several national news outlets. &nbsp;He has been Featured in numerous publications and has trained thousands to protect themselves and their homes from thugs and thieves. He is certified by both the NFSA &amp; the NWDLA as a firearms instructor. &nbsp;He is also an NFSA Range Safety Officer and Defensive Pistol Instructor. He often says: "My students are like family so I take their security personal. &nbsp;I want them to feel confident that they can protect themselves and their families!"</p>
<div class="seen-band abs"></div>
<div class="seen-label display abs"><span class="red">As Seen</span> On</div>
<div class="badge abs" style="left:647px"></div>
<div class="badge abs" style="left:743px"></div>
<div class="badge abs" style="left:839px"></div>
<div class="badge abs" style="left:936px"></div>

<h2 class="section-title display abs" style="top:2030px"><span class="red">What Our</span> Customers Say</h2>
<article class="card abs" style="left:88px"><div class="q">&ldquo;</div><p>"I had never held a gun when I took the Brisklane Wardens Carry class and I'm hooked! I'm going all the way to level 7! &nbsp;Thank you Brisklane Wardens!</p><div class="stars">★★★★★</div><div class="who">Angela M.</div><div class="when">October 14, 2017</div></article>
<article class="card abs" style="left:440px"><div class="q">&ldquo;</div><p>"I was mugged here in Jacksonville and lived in fear ever since. &nbsp;It stole my happiness and I became scared to go out. &nbsp;I'm a Level 4 student and I feel sorry for the next thug that tries me!"</p><div class="stars">★★★★★</div><div class="who">Tawana S.</div><div class="when">December 9, 2017</div></article>
<article class="card abs" style="left:793px"><div class="q">&ldquo;</div><p>"I've been shooting for years and already had my concealed weapons license. &nbsp;My first class was a gun shop class and a waste of money. &nbsp;Morgan took the time to show me how to properly grip my gun and my shooting dramatically improved!</p><div class="stars">★★★★★</div><div class="who">Bill G.</div><div class="when">March 3 2018</div></article>
<div class="pill pill-outline abs" style="left:495px;top:2448px;width:208px">READ MORE TESTIMONIALS</div>

<div class="contact-band abs"></div>
<h2 class="section-title display abs" style="top:2631px"><span class="red">Have</span> Questions?</h2>
<div class="q-item abs" style="left:216px">
  <svg width="52" height="52" viewBox="0 0 52 52"><path d="M14 8l7 9-4 5c3 6 7 10 13 13l5-4 9 7-4 6c-14 0-32-18-32-32z" fill="none" stroke="#222" stroke-width="2.5" stroke-linejoin="round"/><path d="M32 8a14 14 0 0 1 12 12M32 15a7 7 0 0 1 5 5" fill="none" stroke="#e5201f" stroke-width="2.5"/></svg>
  <div class="l1">Call Us</div><div>555-310-4BLW (4259)</div></div>
<div class="q-item abs" style="left:503px">
  <svg width="56" height="52" viewBox="0 0 56 52"><rect x="4" y="6" width="40" height="28" fill="none" stroke="#222" stroke-width="2.5"/><path d="M14 34v10l10-10" fill="none" stroke="#222" stroke-width="2.5"/><path d="M12 15h24M12 22h18" stroke="#e5201f" stroke-width="2.5"/><path d="M44 18h8v24h-8l-6 6v-6" fill="none" stroke="#222" stroke-width="2.5"/></svg>
  <div class="l1">Start a</div><div>Conversation</div></div>
<div class="q-item abs" style="left:744px">
  <svg width="52" height="52" viewBox="0 0 52 52"><path d="M4 22l22-16 22 16v24H4z" fill="none" stroke="#222" stroke-width="2.5" stroke-linejoin="round"/><path d="M4 22l22 16 22-16" fill="none" stroke="#222" stroke-width="2.5"/><path d="M18 20h16M18 26h16" stroke="#e5201f" stroke-width="2.5"/></svg>
  <div class="l1">Send an</div><div>Email</div></div>
<div class="field abs" style="left:209px;top:2851px;width:245px;height:28px">Name</div>
<div class="field abs" style="left:476px;top:2851px;width:246px;height:28px">Email</div>
<div class="field abs" style="left:744px;top:2851px;width:247px;height:28px">Phone</div>
<div class="field abs" style="left:209px;top:2903px;width:782px;height:124px;padding-top:12px">Type your Message ...</div>
<div class="send btn-red abs">SEND MESSAGE</div>

<footer class="footer abs"></footer>
<div class="f-brand abs"><i></i>Brisklane Wardens</div>
<p class="f-about abs" style="color:#ddd">NFSA firearms instructor, NWDLA instructor &amp; training counsellor, news correspondent, and security expert</p>
<div class="f-head abs" style="left:367px;top:3220px">CONTACT US</div>
<div class="f-call abs">Call: 555-310-4BLW (4259)</div>
<div class="f-mail abs">hello@brisklanewardens.example.com</div>
<div class="f-head abs" style="left:367px;top:3324px">BRISKLANE WARDENS</div>
<div class="f-addr abs" style="color:#ddd">P.O. Box 4120 Harbor Point,<br>FL 32990</div>
<div class="f-head abs" style="left:713px;top:3220px">QUICK LINK</div>
<ul class="f-list abs" style="left:713px;top:3252px;color:#ddd"><li>Home</li><li class="on">Falcon Institute</li><li>About</li><li>Testimonials</li><li>Shop</li><li>Upcoming Classes</li><li>Videos</li><li>Lost Certificate</li></ul>
<div class="f-head abs" style="left:864px;top:3220px">MEMBERSHIP</div>
<ul class="f-list abs" style="left:864px;top:3252px;color:#ddd"><li>Benefits &amp; Pricing</li><li>Reviews &amp; Member Stories</li><li>Member Account Login</li><li>Guardian Pathway</li><li>Defensive Carry Journal</li></ul>
<div class="social abs" style="top:3220px" aria-label="Social profile"></div>
<div class="social fill abs" style="top:3263px" aria-label="Social profile"></div>
<div class="social abs" style="top:3304px" aria-label="Social profile"></div>
<div class="social abs" style="top:3345px" aria-label="Social profile"></div>
<div class="f-rule abs"></div>
<div class="copy abs" style="color:#ddd">© 2021 Brisklane Wardens. All Rights Reserved</div>
<div class="to-top abs"><svg width="32" height="32" viewBox="0 0 32 32"><path d="M11 19l5-6 5 6" fill="none" stroke="#fff" stroke-width="2"/></svg></div>

</body>
</html>
```